Suspended swing stage rental

We rent suspended swing stages, rigging soultions set up, teardown and operate.

Change the verbage around
When your crew requires versatile exterior access to a high-rise building, Crestwick Rentals Scaffolding Services can provide you with the suspended scaffolding rental you need to focus on the job at hand. Our experts create swing stage packages for access to buildings and other structures with various shapes, contours, and complex angles for use in a variety of commercial applications.

```html
<!DOCTYPE html>
<html lang="en">
<head>
<meta charset="utf-8">
<title>Crestwick Rentals Scaffolding Services – Flyer</title>
<link href="https://fonts.googleapis.com/css2?family=Poppins:wght@300;400;500;700;800&display=swap" rel="stylesheet">
<style>
  :root{
    --maroon:#5a1230;
    --maroon-deep:#43102a;
    --ink:#1c1c1c;
    --grey-text:#5b5b5b;
    --bar-grey:#6f6f6f;
    --web-bar:#8d8d8d;
    --gold:#c9982f;
    --white:#ffffff;
    --page:#b4b4b4;
  }
  *{box-sizing:border-box;margin:0;padding:0}
  html,body{width:800px;height:1200px;overflow:hidden;background:var(--page);font-family:'Poppins',sans-serif}
  .flyer{position:absolute;left:20px;top:107px;width:760px;height:986px;background:var(--white);overflow:hidden;box-shadow:0 4px 14px rgba(0,0,0,.25)}
  .abs{position:absolute}
  .hero-photo{left:0;top:0;width:760px;height:646px}
  .brand{left:48px;top:52px;display:flex;align-items:center;gap:10px}
  .brand-square{width:26px;height:26px;background:var(--maroon)}
  .brand-name{font-weight:800;font-size:38px;color:var(--maroon);letter-spacing:1px;line-height:1}
  .title{left:46px;top:160px;line-height:46px;font-size:57px;color:var(--maroon);font-weight:800;letter-spacing:-.5px}
  .title .light{font-weight:300;color:var(--grey-text);letter-spacing:0}
  .title-rule{left:52px;top:312px;width:52px;height:3px;background:var(--ink)}
  .lead{left:51px;top:340px;font-weight:800;font-size:19.5px;line-height:20px;color:var(--maroon)}
  .lead-bar{left:50px;top:388px;width:298px;height:27px;background:var(--bar-grey);color:var(--white);font-size:18px;letter-spacing:3.2px;line-height:27px;padding-left:18px;font-weight:400}
  .intro{left:51px;top:426px;font-size:14.6px;line-height:17px;color:var(--ink);white-space:nowrap}
  .band{left:0;top:645px;width:760px;height:341px;background:linear-gradient(135deg,var(--maroon) 0%,var(--maroon-deep) 100%)}
  .rent-title{left:53px;top:678px;font-size:30px;color:var(--white);font-weight:300;line-height:34px}
  .rent-title b{font-weight:700}
  .rent-list{left:50px;top:724px;list-style:none}
  .rent-item{display:flex;align-items:center;height:58px;color:var(--white);font-weight:700;font-size:17.5px}
  .rent-icon{width:48px;height:48px;margin-right:12px;flex:none}
  .divider{left:365px;top:668px;width:1px;height:238px;background:rgba(201,152,47,.45)}
  .about{left:401px;top:682px;font-size:14.6px;line-height:17px;color:var(--white);white-space:nowrap}
  .quality{left:402px;top:785px;font-weight:800;font-size:35px;line-height:32px;color:var(--white)}
  .quality small{display:block;font-weight:500;font-size:17px;letter-spacing:2.4px;color:var(--gold);line-height:24px;margin-top:2px}
  .badge{left:578px;top:768px;width:134px;height:134px}
  .contact{top:932px;font-size:16px;color:var(--white);display:flex;align-items:center;gap:5px}
  .contact.phone{left:36px}
  .contact.email{left:185px}
  .web-bar{left:402px;top:915px;width:358px;height:33px;background:var(--web-bar);clip-path:polygon(14px 0,100% 0,100% 100%,0 100%)}
  .web-text{left:402px;top:915px;width:358px;height:33px;line-height:33px;text-align:center;color:var(--white);font-size:21px;letter-spacing:4px;font-weight:400}
  .web-text b{font-weight:800}
</style>
</head>
<body>
<main class="flyer">
  <svg class="abs hero-photo" viewBox="0 0 760 646" role="img" aria-label="Photo of a high-rise facade with a suspended swing stage and workers, blue sky with clouds">
    <defs>
      <linearGradient id="sky" x1="0" y1="0" x2="1" y2="0.6">
        <stop offset="0" stop-color="#ffffff"/>
        <stop offset="0.45" stop-color="#d9e9f7"/>
        <stop offset="1" stop-color="#9cc6ea"/>
      </linearGradient>
      <linearGradient id="building" x1="0" y1="0" x2="1" y2="0">
        <stop offset="0" stop-color="#8f9092"/>
        <stop offset="0.35" stop-color="#4a4d55"/>
        <stop offset="0.75" stop-color="#c9cbcc"/>
        <stop offset="1" stop-color="#5d8ea0"/>
      </linearGradient>
    </defs>
    <rect width="760" height="646" fill="url(#sky)" opacity="0.75"/>
    <rect width="380" height="646" fill="#ffffff" opacity="0.6"/>
    <polygon points="503,0 760,0 760,646 425,646" fill="url(#building)"/>
  </svg>

  <div class="abs brand"><span class="brand-square"></span><span class="brand-name">CRESTWICK</span></div>

  <h1 class="abs title">RENTALS<br>SCAFFOLDING<br><span class="light">SERVICES</span></h1>
  <div class="abs title-rule"></div>

  <h2 class="abs lead">WHEN YOUR CREW REQUIRES<br>VERSATILE EXTERIOR ACCESS TO</h2>
  <div class="abs lead-bar">A HIGH-RISE BUILDING</div>

  <p class="abs intro">Crestwick Rentals Scaffolding Services<br>can provide you with the suspended scaffolding<br>rental you need to focus on the job at hand.</p>

  <section class="abs band"></section>

  <svg class="abs" style="left:48px;top:502px" width="364" height="156" viewBox="0 0 364 156">
    <polygon points="14,0 184,0 172,156 0,156" fill="#fff"/>
    <polygon points="18,2 180,2 169,152 4,152" fill="#9a9a8a" role="img" aria-label="Photo of the crew in hi-vis vests assembling swing stage equipment in a warehouse"/>
    <polygon points="192,0 364,0 348,144 174,144" fill="#fff"/>
    <polygon points="196,2 360,2 345,140 179,140" fill="#3f7fd0" role="img" aria-label="Photo of a rooftop davit arm rigging against a blue sky"/>
  </svg>

  <h3 class="abs rent-title">WE <b>RENT</b></h3>
  <ul class="abs rent-list">
    <li class="rent-item">
      <svg class="rent-icon" viewBox="0 0 48 48"><circle cx="24" cy="24" r="23" fill="#d9d9d9"/><circle cx="24" cy="24" r="18" fill="#fff"/><line x1="24" y1="10" x2="24" y2="24" stroke="var(--maroon)" stroke-width="2"/><circle cx="21" cy="27" r="3" fill="var(--maroon)"/><rect x="17" y="32" width="14" height="4" fill="var(--maroon)"/></svg>
      Suspended swing stages
    </li>
    <li class="rent-item">
      <svg class="rent-icon" viewBox="0 0 48 48"><circle cx="24" cy="24" r="23" fill="#d9d9d9"/><circle cx="24" cy="24" r="18" fill="#fff"/><path d="M20 13h8l4 22H16z" fill="none" stroke="var(--maroon)" stroke-width="2.4"/><line x1="18" y1="22" x2="30" y2="22" stroke="var(--maroon)" stroke-width="2"/><line x1="17" y1="29" x2="31" y2="29" stroke="var(--maroon)" stroke-width="2"/></svg>
      Rigging solutions set up
    </li>
    <li class="rent-item">
      <svg class="rent-icon" viewBox="0 0 48 48"><circle cx="24" cy="24" r="23" fill="#d9d9d9"/><circle cx="24" cy="24" r="18" fill="#fff"/><circle cx="24" cy="24" r="9" fill="none" stroke="var(--maroon)" stroke-width="5" stroke-dasharray="4 3"/><circle cx="24" cy="24" r="3.5" fill="var(--maroon)"/></svg>
      Teardown and operate
    </li>
  </ul>

  <div class="abs divider"></div>

  <p class="abs about">Our experts create swing stage packages<br>for access to buildings and other<br>structures with various shapes, contours,<br>and complex angles for use in a variety<br>of commercial applications.</p>

  <div class="abs quality">HIGH<br>QUALITY<small>WORKMANSHIP</small></div>

  <svg class="abs badge" viewBox="0 0 134 134" role="img" aria-label="Anniversary badge">
    <path d="M67 6 L116 22 L114 78 Q108 110 67 128 Q26 110 20 78 L18 22 Z" fill="var(--gold)"/>
  </svg>

  <div class="abs contact phone">
    <svg width="14" height="14" viewBox="0 0 24 24"><path d="M6.6 10.8a15 15 0 0 0 6.6 6.6l2.2-2.2c.3-.3.7-.4 1-.2 1.1.4 2.3.6 3.6.6.6 0 1 .4 1 1V20c0 .6-.4 1-1 1A17 17 0 0 1 3 4c0-.6.4-1 1-1h3.5c.6 0 1 .4 1 1 0 1.3.2 2.5.6 3.6.1.3 0 .7-.2 1z" fill="#bbb"/></svg>
    555.014.2270
  </div>
  <div class="abs contact email">
    <svg width="16" height="12" viewBox="0 0 16 12"><rect x="0.5" y="0.5" width="15" height="11" fill="none" stroke="#bbb"/><path d="M1 1l7 6 7-6" fill="none" stroke="#bbb"/></svg>
    info@crestwick.net
  </div>

  <div class="abs web-bar"></div>
  <div class="abs web-text">www.<b>crestwick</b>.net</div>
</main>
</body>
</html>
```